Web Design / Transformation our Joomla web site

Job Type
We are looking for a fresh eye-catching Custom Joomla Design to transform our Joomla web site

Task Description
We are in a process to create web site to Speech Pathology services . The site is built by using brightframe ((http://www.brightframe-example.com/) meadow template.

You can see our site http://littlelanternspeech-example.com/demo

Unfortunately, this template does not match our identity. We would like to improve or replace it. Although we like features that brightframe template is giving as part of their template ,we want to transform our site to something more simplistic and kids oriented . We don’t like look and fill of our website since it’s very professional and “corporate” . Our business is very small and is not 100 people company , we are looking for something more simple and personal. It should look professional, all be it, child friendly. We work on children’s communication skills, and we want to convey an idea that communication is “Little Lantern”, meaning children need to learn to play and socialize appropriately. In addition, learning to be a better communicators will help them to be closer to their family members and friends. We want our website to show kids playing and having fun. In other hand , we don't want the Website to be too busy with images, so use your professional judgment.
You can change current template or you can provide your own Joomla design.

Examples of website look that we like :

http://tinytalkerhub-example.com
http://chattergardenpals-example.com/
http://wrenvoicelessons-example.com/

About Our Company :
Company name: Little Lantern
What we do: Pediatric Speech & Language Pathology Services. We established Little Lantern to provide families with a unique option for their child’s speech therapy needs. Our clinic is founded on the principle that all children are different and require a thoughtful, parent-driven therapy plan. When a family chooses us, they will enter a partnership with an experienced, well-trained therapist.
Top Three Things to Communicate through our Website:
#1 - We are kids friendly
#2 - We are professional
#3 - We provide our services with a loving, nurturing attitude toward the child and with compassionate, comprehensive support and input for the family
Updates

To see current running site : http://littlelanternspeech-example.com/demo/

Reason: There are no good designs to address our needs

Reason: It's still work in progress. Submitted designs are still under constructions and waiting for updates

We are accepting WordPress designs as well !!!

Target Market(s)

Families with kids

Industry/Entity Type

Communication

Requirements
Must have
• • Joomla/Wordpress as a platform
• Easy to Navigate
• Clean Design, kids friendly but professional

```html
<!DOCTYPE html>
<html lang="en">
<head>
<meta charset="utf-8">
<title>Little Lantern – Speech &amp; Language Pathology Services</title>
<link rel="stylesheet" href="https://fonts.googleapis.com/css2?family=Ubuntu:wght@400;500;700&family=Gelasio:wght@400&family=Fredoka:wght@600&display=swap">
<style>
  :root {
    --sky-top: #bfe6f3;
    --sky-mid: #e3f4fa;
    --sky-low: #f4fbfd;
    --grass: #7cc236;
    --grass-dark: #5ea521;
    --nav-red: #ff3a0a;
    --nav-red-dark: #e21c00;
    --slider-green: #8bcf1b;
    --slider-green-dark: #5f9f08;
    --dot-blue: #2a8fe0;
    --dot-red: #e0101a;
    --ink: #222222;
    --heading: #1e1e1e;
    --button: #00b4ef;
    --rule: #9a9a9a;
    --panel-line: #dddddd;
    --brand-blue: #1f8fe0;
    --white: #ffffff;
  }
  * { box-sizing: border-box; margin: 0; padding: 0; }
  html, body { width: 1200px; height: 1063px; overflow: hidden; background: var(--white); }
  body { position: relative; font-family: "Ubuntu", sans-serif; color: var(--ink); }

  .sky {
    position: absolute; left: 0; top: 0; width: 1200px; height: 440px;
    background: linear-gradient(180deg, var(--sky-top) 0%, var(--sky-mid) 45%, var(--sky-low) 80%);
  }
  .hill {
    position: absolute; left: 0; top: 395px; width: 1200px; height: 45px;
    background: linear-gradient(180deg, var(--grass) 0%, var(--grass-dark) 100%);
  }

  .brand { position: absolute; left: 137px; top: 60px; width: 230px; }
  .brand-name {
    display: flex; align-items: center; gap: 10px;
    font-family: "Fredoka", sans-serif; font-weight: 600; font-size: 38px;
    color: var(--brand-blue); line-height: 1;
  }
  .brand-dot { width: 22px; height: 22px; border-radius: 50%; background: var(--nav-red); flex: none; }
  .brand-tagline {
    margin-top: 58px; font-family: "Ubuntu", sans-serif; font-weight: 500;
    font-size: 11px; color: var(--brand-blue); white-space: nowrap;
  }

  .main-nav {
    position: absolute; left: 507px; top: 137px; width: 592px; height: 40px;
    border-radius: 12px; border: 2px solid var(--nav-red-dark);
    background: linear-gradient(180deg, #ff6a2a 0%, var(--nav-red) 55%, var(--nav-red-dark) 100%);
    display: flex; align-items: center; justify-content: center;
  }
  .main-nav a {
    color: var(--white); text-decoration: none; font-weight: 700; font-size: 13px;
  }
  .main-nav .sep { color: var(--white); font-weight: 700; font-size: 13px; margin: 0 12px; }

  .slider {
    position: absolute; left: 110px; top: 209px; width: 988px; height: 433px;
    border-radius: 14px;
    background: linear-gradient(180deg, var(--slider-green) 0%, var(--slider-green-dark) 100%);
  }
  .slide {
    position: absolute; left: 28px; top: 27px; width: 932px; height: 332px;
    border-radius: 8px; border: 3px solid #f2f8e6;
    background: linear-gradient(100deg, #e7d4bf 0%, #f3ede6 35%, #fbf7f2 60%, #dcc3a4 100%);
  }
  .slider-dots { position: absolute; left: 435px; top: 393px; display: flex; gap: 11px; }
  .slider-dots span {
    width: 19px; height: 19px; border-radius: 50%;
    background: var(--dot-blue); border: 2px solid #d8ecff;
  }
  .slider-dots span.active { background: var(--dot-red); border-color: #ffd2d2; }

  .welcome { position: absolute; left: 121px; top: 674px; width: 642px; }
  .welcome h1 {
    font-family: "Gelasio", serif; font-weight: 400; font-size: 24px; color: var(--heading);
    padding-bottom: 5px; border-bottom: 1px dashed var(--rule);
  }
  .welcome p { font-size: 13px; line-height: 17px; margin-top: 16px; }
  .welcome p:first-of-type { margin-top: 10px; }
  .read-more {
    display: inline-block; margin-top: 31px; width: 102px; height: 31px; line-height: 31px;
    text-align: center; background: var(--button); color: var(--white);
    font-weight: 500; font-size: 13px; text-decoration: none;
  }

  .recent-posts {
    position: absolute; left: 820px; top: 683px; width: 278px; height: 374px;
    border: 1px solid #cfcfcf; border-radius: 12px;
    background: linear-gradient(180deg, #ffffff 0%, #ffffff 70%, #eeeeee 100%);
  }
  .recent-posts h2 {
    font-family: "Gelasio", serif; font-weight: 400; font-size: 24px; text-align: center;
    color: var(--heading); height: 55px; line-height: 55px;
    box-shadow: 0 8px 10px -8px rgba(0,0,0,0.15);
  }
  .recent-posts ul { list-style: none; margin: 20px 20px 0 18px; }
  .recent-posts li {
    position: relative; padding: 8px 0 8px 12px; font-size: 12.5px; line-height: 16px;
    border-bottom: 1px solid var(--panel-line);
  }
  .recent-posts li::before {
    content: ""; position: absolute; left: 0; top: 50%; margin-top: -5px;
    border-left: 6px solid #111; border-top: 5px solid transparent; border-bottom: 5px solid transparent;
  }
  .recent-posts li:last-child { border-bottom: none; }
</style>
</head>
<body>
  <div class="sky" role="img" aria-label="Illustrated sky with soft clouds and a rainbow"></div>
  <div class="hill" role="img" aria-label="Green grassy hill"></div>

  <header>
    <div class="brand">
      <div class="brand-name"><span class="brand-dot"></span>Little Lantern</div>
      <div class="brand-tagline">Speech &amp; Language Pathology Services</div>
    </div>
    <nav class="main-nav">
      <a href="#">Home</a><span class="sep">|</span>
      <a href="#">About</a><span class="sep">|</span>
      <a href="#">Treatment Techniques</a><span class="sep">|</span>
      <a href="#">Blog</a><span class="sep">|</span>
      <a href="#">FAQ</a><span class="sep">|</span>
      <a href="#">Resources</a><span class="sep">|</span>
      <a href="#">Contact</a>
    </nav>
  </header>

  <section class="slider">
    <div class="slide" role="img" aria-label="Photo of a mother hugging her smiling daughter on a white sofa"></div>
    <div class="slider-dots"><span class="active"></span><span></span><span></span><span></span><span></span></div>
  </section>

  <main class="welcome">
    <h1>welcome to Little Lantern</h1>
    <p>Speech Therapy in Plano, Frisco, Allen , McKineey ,Dallas, Richardson &amp; all of North Texas</p>
    <p>My name is Mara Feldstone. I am a speech pathologists , and I am also a mother of three kids: two girls and a boy.</p>
    <p>Welcome to my site.</p>
    <p>I also frequently search the Internet to find a school, camp, classes and therapies for my own kids. I know that a task of finding a place and people who I can trust my kids is not an easy task.</p>
    <p>Whenever I look for a teacher/coach /therapist for my children, I want someone who has experience, knowledge, and expertise in their area. I also want them to be passionate, loving, accepting, and fun, but most importantly I want this person &nbsp;to appreciate my child for who she/ he is , see the possibilities , the strengths, love my child , and be optimistic about his/ her future. &nbsp;I don't expect this teacher/coach/ therapist to know all the answers, but I expect her to be determined to do what it takes to find the solutions.</p>
    <a class="read-more" href="#">Read More</a>
  </main>

  <aside class="recent-posts">
    <h2>Recent Posts</h2>
    <ul>
      <li>My Little Hero</li>
      <li>Better Hearing and Speech Month Freebies!</li>
      <li>Freebie: SKW Cluster Game for Spring!</li>
      <li>My Lily Rose Is Getting Well</li>
      <li>New Speech Therapy Spring Freebie</li>
      <li>From the blog, “Little Voices Speech!”</li>
    </ul>
  </aside>
</body>
</html>
```